Require a Business card , letter head and envelope for my company named Quiet amber,

Quiet amber is a trading company dealing with multiple products in the following categories. Home , kitchen, furniture, Grocery, health. fitness etc.
I am attaching the logo designed by gigmarket .in.
The business card should include the Following
1)name :Suresh M T
2)Designation : VP Product Innovation
3)Mobile no +91 7045518360
4)Emailid :suresh@quietamber .com
5)Web site: quietamber.com
6) Company Logo
7) Company address( can be on the reverse side also): Quiet amber, 41/512B, VLMS Road, Kottamala, Calicut 673019, Kerala , India
The letter head and envelope, should include the following ,
Logo , Email id , Web site address ,and the postal address.

```html
<!DOCTYPE html>
<html lang="en">
<head>
<meta charset="utf-8">
<title>Quiet amber – Business Card</title>
<link rel="stylesheet" href="https://fonts.googleapis.com/css2?family=Montserrat:wght@700&family=Roboto:wght@400;700&display=swap">
<style>
  :root {
    --stage: #e9e9eb;
    --paper: #ffffff;
    --ink: #141414;
    --red: #e8222c;
    --faint: #f1f1f1;
    --muted: #2b2b2b;
  }
  * { box-sizing: border-box; margin: 0; padding: 0; }
  html, body { width: 1200px; height: 900px; overflow: hidden; }
  body {
    background: var(--stage);
    font-family: "Roboto", Arial, sans-serif;
    color: var(--ink);
    display: flex;
    flex-direction: column;
    align-items: center;
    justify-content: center;
    gap: 40px;
  }
  .card {
    position: relative;
    width: 700px;
    height: 400px;
    background: var(--paper);
    overflow: hidden;
    box-shadow: 0 6px 18px rgba(0,0,0,0.18);
  }
  .band { position: absolute; left: 0; right: 0; }
  .card-front .band { background: var(--ink); height: 20px; }
  .card-back .band-top { background: var(--red); height: 16px; top: 0; }
  .card-back .band-bottom { background: var(--red); height: 24px; bottom: 0; }
  .band-top { top: 0; }
  .band-bottom { bottom: 0; }

  .faint-mark {
    position: absolute;
    border-radius: 50%;
    background: var(--faint);
  }
  .card-front .faint-mark { width: 190px; height: 190px; left: 170px; top: 70px; }
  .card-back .faint-mark { width: 120px; height: 120px; left: 330px; top: 70px; }

  .brand {
    display: flex;
    align-items: center;
    gap: 12px;
    font-family: "Montserrat", Arial, sans-serif;
    font-weight: 700;
    color: var(--ink);
    letter-spacing: 0.5px;
  }
  .brand-dot { border-radius: 50%; background: var(--red); flex: none; }

  .front-content {
    position: absolute;
    inset: 0;
    display: flex;
    flex-direction: column;
    align-items: center;
    justify-content: center;
    gap: 22px;
  }
  .front-content .brand { font-size: 40px; }
  .front-content .brand-dot { width: 46px; height: 46px; }
  .website { font-size: 22px; color: var(--ink); }

  .identity { position: absolute; left: 42px; top: 92px; }
  .person-name { font-size: 30px; font-weight: 700; color: var(--red); }
  .person-title { font-size: 13px; font-weight: 700; margin-top: 2px; }

  .contacts {
    position: absolute;
    left: 42px;
    top: 180px;
    list-style: none;
    display: flex;
    flex-direction: column;
    gap: 12px;
  }
  .contact { display: flex; align-items: flex-start; gap: 14px; font-size: 16px; line-height: 1.3; color: var(--muted); }
  .contact svg { flex: none; width: 26px; height: 26px; }

  .card-back .brand {
    position: absolute;
    right: 38px;
    top: 110px;
    flex-direction: column;
    gap: 8px;
    font-size: 17px;
  }
  .card-back .brand-dot { width: 40px; height: 40px; }
</style>
</head>
<body>

  <section class="card card-front" aria-label="Business card front">
    <div class="band band-top"></div>
    <div class="faint-mark"></div>
    <div class="front-content">
      <div class="brand"><span class="brand-dot"></span>QUIET AMBER</div>
      <p class="website">www.quietamber.com</p>
    </div>
    <div class="band band-bottom"></div>
  </section>

  <section class="card card-back" aria-label="Business card back">
    <div class="band band-top"></div>
    <div class="faint-mark"></div>

    <div class="identity">
      <h1 class="person-name">Suresh M T</h1>
      <p class="person-title">VP Product Innovation</p>
    </div>

    <ul class="contacts">
      <li class="contact">
        <svg viewBox="0 0 26 26" aria-hidden="true">
          <circle cx="13" cy="13" r="11.5" fill="none" stroke="var(--red)" stroke-width="2"/>
          <path d="M9 7.5l2.2 0 1 3-1.5 1.2a7 7 0 0 0 3.6 3.6l1.2-1.5 3 1 0 2.2c0 .8-.7 1.4-1.5 1.3A10 10 0 0 1 7.7 9c-.1-.8.5-1.5 1.3-1.5z" fill="var(--ink)"/>
        </svg>
        <span>+91 7045518360</span>
      </li>
      <li class="contact">
        <svg viewBox="0 0 26 26" aria-hidden="true">
          <circle cx="13" cy="13" r="12" fill="var(--red)"/>
          <rect x="7" y="8.5" width="12" height="9" rx="1" fill="#fff"/>
          <path d="M7.5 9l5.5 4.5 5.5-4.5" fill="none" stroke="var(--red)" stroke-width="1.4"/>
        </svg>
        <span>suresh@quietamber.com<br>quietamber.com</span>
      </li>
      <li class="contact">
        <svg viewBox="0 0 26 26" aria-hidden="true">
          <circle cx="13" cy="13" r="12" fill="var(--red)"/>
          <path d="M13 5.5a5 5 0 0 0-5 5c0 3.6 5 9.5 5 9.5s5-5.9 5-9.5a5 5 0 0 0-5-5z" fill="#fff"/>
          <circle cx="13" cy="10.5" r="1.8" fill="var(--red)"/>
        </svg>
        <span>Quiet amber, 41/512B, VLMS Road, Kottamala,<br>Calicut 673019, Kerala, India.</span>
      </li>
    </ul>

    <div class="brand"><span class="brand-dot"></span>QUIET AMBER</div>
    <div class="band band-bottom"></div>
  </section>

</body>
</html>
```